Book Cover for Christian Book titled, "Climbing Past the Silver Hills"

Size of book cover will be 6" x 9".
The book is about how a person can know beyond a shadow of a doubt that they will go to heaven when they die.
The Title is "Climbing Past the Silver Hills"
Subtitle is "Finding Lasting Peace Through Daily Quiet Prayer and Reflection."
The front of the book should have title, subtitle, and author. The back of the book and spine should have no text and be a solid color.
The uploaded pic is a possibility for a design; but I'm open to other designs.
Whatever images are used need to be very high quality to meet Marrowind Folio Services guidelines. Also, the finished product needs to be sized to match the MFS guide for a 6x9 book.

```html
<!DOCTYPE html>
<html lang="en">
<head>
<meta charset="utf-8">
<title>Climbing Past the Silver Hills — Front Cover</title>
<link rel="stylesheet" href="https://fonts.googleapis.com/css2?family=Playfair+Display+SC:wght@400;700&family=Federo&display=swap">
<style>
  :root {
    --sky-white: #fbfcfd;
    --sky-grey: #dfe2e6;
    --sky-gold: #f1e07a;
    --horizon-yellow: #f3e56e;
    --field-green: #3f8a2d;
    --field-dark: #2c6a1f;
    --title-navy: #2f4d8e;
    --title-teal: #3aa9c4;
    --band-yellow: #f6ec68;
    --subtitle-navy: #2e3f86;
    --author-white: #ffffff;
  }
  * { margin: 0; padding: 0; box-sizing: border-box; }
  html, body {
    width: 800px;
    height: 1200px;
    overflow: hidden;
    background: var(--sky-white);
  }
  .cover {
    position: relative;
    width: 800px;
    height: 1200px;
    overflow: hidden;
  }
  .cover-photo {
    position: absolute;
    inset: 0;
    background: linear-gradient(to bottom,
      var(--sky-white) 0%,
      var(--sky-white) 14%,
      var(--sky-grey) 40%,
      var(--sky-gold) 62%,
      var(--horizon-yellow) 80%,
      var(--field-green) 83%,
      var(--field-dark) 100%);
  }
  .title {
    position: absolute;
    left: 0;
    top: 0;
    width: 800px;
    height: 460px;
  }
  .title text {
    font-family: "Playfair Display SC", "Bodoni Moda", serif;
  }
  .subtitle-band {
    position: absolute;
    left: 80px;
    top: 462px;
    width: 630px;
    height: 96px;
    background: var(--band-yellow);
    filter: blur(9px);
    opacity: 0.95;
  }
  .subtitle {
    position: absolute;
    left: 90px;
    top: 478px;
    width: 620px;
    text-align: center;
    font-family: "Federo", sans-serif;
    font-size: 25px;
    line-height: 31px;
    letter-spacing: 1.8px;
    color: var(--subtitle-navy);
  }
  .author {
    position: absolute;
    left: 0;
    top: 1100px;
    width: 800px;
    text-align: center;
    font-family: "Federo", sans-serif;
    font-size: 30px;
    letter-spacing: 4px;
    color: var(--author-white);
  }
</style>
</head>
<body>
  <main class="cover">
    <div class="cover-photo" role="img" aria-label="Photograph of the sun breaking through clouds over a wide green field"></div>

    <svg class="title" viewBox="0 0 800 460" aria-labelledby="book-title">
      <title id="book-title">Climbing Past the Silver Hills</title>
      <defs>
        <linearGradient id="title-fill" x1="0" y1="0" x2="1" y2="1">
          <stop offset="0" stop-color="var(--title-teal)"/>
          <stop offset="0.35" stop-color="var(--title-navy)"/>
          <stop offset="0.6" stop-color="var(--title-teal)"/>
          <stop offset="1" stop-color="var(--title-navy)"/>
        </linearGradient>
      </defs>
      <text x="120" y="172" font-size="72" fill="url(#title-fill)" textLength="556" lengthAdjust="spacingAndGlyphs">CLIMBING PAST</text>
      <text x="120" y="273" font-size="116" fill="url(#title-fill)" textLength="558" lengthAdjust="spacingAndGlyphs">THE SILVER</text>
      <text x="120" y="438" font-size="204" fill="url(#title-fill)" textLength="562" lengthAdjust="spacingAndGlyphs">HILLS</text>
    </svg>

    <div class="subtitle-band"></div>
    <p class="subtitle">Finding Lasting Peace Through Daily<br>Quiet Prayer and Reflection.</p>

    <p class="author">ELIAS MARDEN</p>
  </main>
</body>
</html>
```